Pagevoより「最前線・空腹がすっと静まる献立&噛み方の手引き」というタイトルの電子書籍を出版予定です。

この本のコンセプトは「食べ物を選んで食べること&その食べ方で食欲が自然におさまること、更にはそれがダイエットと健康維持とアンチエイジングに非常に効果的であること、プラス今流行りのダイエット方(オートファジーダイエット、ミトコンドリア活性化、ケトジェニックダイエット、16時間断食、レクチンフリー 食品の勧め、腸活、SATエクササイズ、オイルの種類など)の説明とご提案(やり方)」をお伝えし、読者の皆様の健康維持に貢献したいということです。

ターゲットは男女ともに考えております。デザインは明るくて「何これ、ダイエットや食品の本にしては発想が新しい!」と興味を持ってもらえることを期待しております。(抽象的ですみません;)

何かご質問・ご提案がありましたらいつでもご連絡ください。
どうぞ宜しくお願いいたします。
*以下2項目の追加記載をお願いいたします。お手数ですがどうぞ宜しくお願いいたします。

・読者プレゼント
星座タイプ別 きみに向く減量術と献立チェック

・著者名: 森川 結奈
皆様、お忙しいところをたくさんのご応募、ありがとうございました!
どれも素敵なデザインでなかなか決めるのが難しいところではありますが、
数日中に決定、上位3名の方にご連絡いたします。

それでは、どうぞしばらくお待ちくださいませ。

取り急ぎ、お礼まで。

Thank you so much!
森川 結奈

当選:miru72_studio様 ー 明るくてフレッシュで清潔感のあるイメージで、何だろう?と書店だったら思わず手に取りたくなる素敵なデザインだと思いました。 次点:ripple_308様 ー デザインが可愛いく親しみやすいのと「食事を抑えるのでなく食欲を抑えるダイエット」など刺さるコピーがとても鋭いと感じました。執筆仲間にも好評でした。 次点: Hnbrook様 ー シンプルで見やすいが故に、逆に何が書いてあるんだろう?と興味を持たせてくれそうなデザインだと感じました。仲間内でも好評でした。

選定が遅くなり大変申し訳ございませんでした。この度は沢山の素敵なデザインをご提案くださり、ありがとうございました。 周りの者と相談の上、悩んだ末に決定させていただきました。 本当に素晴らしい作品ばかりで、デザインをするお仕事の素晴らしさを教えていただきました。 皆様のパワーにインスパイアされ、また二冊目も書きたいと思う原動力をいただきました。 またぜひご縁をいただけたら幸いです。 心より感謝申し上げます。どうもありがとうございました。 皆様のますますのご活躍とご発展をお祈り申し上げます。森川結奈

```html
<!DOCTYPE html>
<html lang="ja">
<head>
<meta charset="utf-8">
<title>最前線・空腹がすっと静まる献立&amp;噛み方の手引き</title>
<link href="https://fonts.googleapis.com/css2?family=Noto+Sans+JP:wght@500;700;900&family=Noto+Serif+JP:wght@700;900&display=swap" rel="stylesheet">
<style>
  :root {
    --paper: #ebe6de;
    --paper-deep: #dcd5ca;
    --brown: #6b4a2c;
    --brown-dark: #4e3520;
    --ink: #1b1714;
    --white: #ffffff;
  }
  * { margin: 0; padding: 0; box-sizing: border-box; }
  html, body { width: 750px; height: 1200px; overflow: hidden; background: var(--paper); }
  .cover {
    position: relative;
    width: 750px;
    height: 1200px;
    overflow: hidden;
    font-family: "Noto Sans JP", sans-serif;
    color: var(--ink);
  }
  .backdrop {
    position: absolute; inset: 0;
    background: radial-gradient(ellipse at 50% 45%, var(--paper) 0%, var(--paper) 55%, var(--paper-deep) 100%);
  }
  .series-mark {
    position: absolute; top: 10px; left: 0; width: 750px;
    text-align: center;
    font-family: "Noto Serif JP", serif;
    font-weight: 900;
    font-size: 104px;
    letter-spacing: 60px;
    padding-left: 60px;
    color: var(--brown-dark);
    line-height: 1.1;
  }
  .ribbon {
    position: absolute; top: 196px; left: 68px;
    width: 614px; height: 70px;
  }
  .ribbon svg { position: absolute; inset: 0; }
  .ribbon-text {
    position: absolute; inset: 0;
    display: flex; align-items: center; justify-content: center;
    color: var(--white);
    font-weight: 700;
    font-size: 42px;
    letter-spacing: 2px;
    padding-bottom: 8px;
  }
  .title-panel {
    position: absolute; top: 268px; left: 100px;
    width: 562px; height: 584px;
    background: var(--white);
    border: 4px solid var(--brown);
    border-radius: 28px;
    text-align: center;
  }
  .title {
    display: flex;
    flex-direction: column;
    align-items: center;
    padding-top: 30px;
  }
  .title-line {
    display: block;
    font-weight: 900;
    color: var(--ink);
    line-height: 1;
  }
  .title-line.main { font-size: 124px; height: 132px; letter-spacing: -2px; }
  .title-line.joint { font-size: 64px; height: 76px; line-height: 76px; font-family: "Noto Serif JP", serif; }
  .title-line.particle { font-size: 62px; height: 76px; line-height: 76px; }
  .cutlery { position: absolute; left: 256px; bottom: 24px; }
  .gift-panel {
    position: absolute; top: 872px; left: 0;
    width: 340px; height: 246px;
    background: var(--white);
    border-radius: 0 24px 24px 0;
    text-align: center;
  }
  .gift-heading {
    padding-top: 16px;
    font-weight: 900;
    font-size: 46px;
    line-height: 1.12;
    color: var(--brown);
  }
  .gift-band {
    margin-top: 10px;
    background: var(--brown);
    color: var(--white);
    font-weight: 700;
    font-size: 26px;
    line-height: 38px;
  }
  .gift-title {
    padding-top: 6px;
    font-weight: 900;
    font-size: 30px;
    line-height: 1.22;
    color: var(--ink);
  }
  .author {
    position: absolute; top: 1058px; left: 480px;
    width: 250px; text-align: center;
    font-weight: 900;
    font-size: 44px;
    color: var(--brown-dark);
  }
  .author small { font-size: 24px; font-weight: 700; margin-left: 6px; }
</style>
</head>
<body>
  <main class="cover">
    <div class="backdrop" role="img" aria-label="淡いベージュ地に野菜や食材の線画イラストが散りばめられた背景"></div>

    <div class="series-mark">最前線</div>

    <div class="ribbon">
      <svg width="614" height="70" viewBox="0 0 614 70" aria-hidden="true">
        <polygon points="0,8 60,8 60,62 0,62 18,35" fill="var(--brown-dark)"/>
        <polygon points="614,8 554,8 554,62 614,62 596,35" fill="var(--brown-dark)"/>
        <rect x="40" y="0" width="534" height="62" fill="var(--brown)"/>
      </svg>
      <div class="ribbon-text">空腹がすっと静まる</div>
    </div>

    <section class="title-panel">
      <h1 class="title">
        <span class="title-line main">献立</span>
        <span class="title-line joint">&amp;</span>
        <span class="title-line main">噛み方</span>
        <span class="title-line particle">の</span>
        <span class="title-line main">手引き</span>
      </h1>
      <svg class="cutlery" width="50" height="14" viewBox="0 0 50 14" aria-hidden="true">
        <line x1="2" y1="7" x2="48" y2="7" stroke="var(--brown)" stroke-width="2"/>
        <circle cx="25" cy="7" r="4" fill="var(--brown)"/>
      </svg>
    </section>

    <aside class="gift-panel">
      <p class="gift-heading">読者<br>プレゼント</p>
      <p class="gift-band">星座タイプ別</p>
      <p class="gift-title">きみに向く<br>減量術と献立チェック</p>
    </aside>

    <p class="author">森川 結奈<small>著</small></p>
  </main>
</body>
</html>
```